Corporate Design für Baumpflege-Holstedt
Zielgruppe
Baumpflege-Holstedt als junges etabliertes Unternehmen sucht nach einem CD. Unser Einsatzgebiet, da wo die anderen nicht hinkommen. In erster Linie Baumpflegearbeiten, die kletternd ausgeführt werden, Kletterarbeiten für Wissenschaft u. Forschung. Zweitrangig werden Baumumfeldverbesserung, Baumkontrolle sowie Baumpflanzungen sowie Forstarbeiten angeboten.
Die Zielgruppe setzt sich aus öffentlichen Auftraggebern, Unternehmen u. privaten Auftraggebern zusammen.
Aufgabenstellung
Design soll Vertrauen, Seriosität u. Bodenständigkeit. Baumpflege-Holstedt steht nicht für den Allrounder der alles kann, es geht um professionelle Baumpflege.

```html
<!DOCTYPE html>
<html lang="de">
<head>
<meta charset="utf-8">
<title>Baumpflege Holstedt – Corporate Design</title>
<link href="https://fonts.googleapis.com/css2?family=Montserrat:wght@500;700;800&family=Arimo:wght@400;700&display=swap" rel="stylesheet">
<style>
  :root{
    --bg:#eeeeec;
    --paper:#ffffff;
    --green:#0a8a4c;
    --green-dark:#0f5c3b;
    --green-light:#6cbf3b;
    --navy:#1f3557;
    --ghost:#f1f2f3;
    --ink:#444a50;
  }
  *{margin:0;padding:0;box-sizing:border-box}
  html,body{width:1200px;height:1200px;overflow:hidden;background:var(--bg)}
  body{position:relative;font-family:"Arimo",Arial,sans-serif;color:var(--ink)}
  .sheet{position:absolute;background:var(--paper);overflow:hidden}
  .sheet.navy{background:var(--navy)}
  .label{position:absolute;font:400 12px "Arimo",Arial,sans-serif;color:#333}

  /* logo lockup: name set in one colour and one weight */
  .logo{position:absolute;display:flex;align-items:center;gap:.5em;font-family:"Montserrat",sans-serif}
  .logo .dot{width:2.4em;height:2.4em;border-radius:50%;background:currentColor;flex:none}
  .logo .name{font-weight:800;line-height:1.05;letter-spacing:.04em;text-transform:uppercase;white-space:nowrap}
  .logo.green{color:var(--green-dark)}
  .logo.lime{color:var(--green-light)}
  .claim{display:block;font:500 .4em "Montserrat",sans-serif;letter-spacing:.14em;text-transform:none;color:#555;margin-top:.5em;white-space:nowrap}
  .logo.lime .claim{color:#ffffff}

  .ghost-mark{position:absolute;border-radius:50%;background:var(--ghost)}
  .band{position:absolute;left:0;right:0;bottom:0;background:var(--green);color:#fff;
        font:700 5px "Montserrat",sans-serif;letter-spacing:.08em;display:flex;align-items:center}
  .band.navy{background:var(--navy)}

  /* letterhead */
  .letterhead{left:180px;top:102px;width:376px;height:531px}
  .letterhead .accent{position:absolute;left:0;top:60px;width:12px;height:54px;background:var(--green)}
  .letterhead .address{position:absolute;left:17px;top:63px;font-size:4.6px;line-height:1.35;color:#555}
  .contact-list{list-style:none;margin-top:4px}
  .contact-list li{display:flex;align-items:center;gap:4px}
  .contact-list svg{width:5px;height:5px;fill:var(--green);flex:none}
  .letterhead .legal{position:absolute;top:499px;font-size:4.4px;line-height:1.3}
  .legal.key{color:var(--green)}
  .legal.val{color:#555}
  .letterhead .band{height:9px;justify-content:center}

  /* business cards */
  .card{width:153px;height:98px}
  .card .details{position:absolute;left:82px;top:22px;font-size:4.3px;line-height:1.3;color:#555}
  .card .details .person{font:500 5.4px "Arimo",Arial,sans-serif;color:#444}
  .card .details .role{color:var(--green);margin-bottom:6px}
  .card.alt .details,.card.alt .details .person{color:var(--navy);font-weight:700}
  .card.alt .contact-list svg{fill:var(--navy)}
  .card .band{height:7px;justify-content:center}

  /* envelopes */
  .envelope{width:393px;height:198px}
  .envelope .band{height:8px;justify-content:flex-end;padding-right:8px}
</style>
</head>
<body>

<!-- Letterhead -->
<section class="sheet letterhead">
  <div class="ghost-mark" style="left:40px;top:230px;width:300px;height:260px"></div>
  <div class="logo green" style="left:218px;top:12px;font-size:9px">
    <i class="dot"></i>
    <div class="name">Baumpflege<br>Holstedt<span class="claim">Kronenpflege mit Seil</span></div>
  </div>
  <div class="accent"></div>
  <div class="address">
    BAUMPFLEGE HOLSTEDT<br>XXXXXXXXXX Str. 00<br>00000 Germany
    <ul class="contact-list">
      <li><svg viewBox="0 0 10 10"><rect x="1" y="3" width="8" height="6" rx="1"/></svg>0000 00 00 00 00</li>
      <li><svg viewBox="0 0 10 10"><rect x="3" y="0" width="4" height="10" rx="1"/></svg>0000 00 00 00 00</li>
      <li><svg viewBox="0 0 10 10"><rect x="1" y="2" width="8" height="7"/></svg>0000 00 00 00 00</li>
      <li><svg viewBox="0 0 10 10"><rect x="0" y="2" width="10" height="6"/></svg>info@baumpflege-holstedt.de</li>
    </ul>
  </div>
  <div class="legal key" style="left:88px">Geschäftsführer<br>USt-ID-Nr<br>steuernummer</div>
  <div class="legal val" style="left:135px">John Doe<br>DE 000 000 000<br>00 000 0000</div>
  <div class="legal key" style="left:188px">BANK<br>IBAN<br>BIC</div>
  <div class="legal val" style="left:234px">XXXXXXXXXX<br>DE00 0000 0000 0000 0000 00<br>XXXXXXXXXX</div>
  <div class="band">www.baumpflege-holstedt.de</div>
</section>

<!-- Logo panels -->
<section class="sheet" style="left:621px;top:106px;width:445px;height:256px">
  <div class="logo green" style="left:60px;top:88px;font-size:26px">
    <i class="dot"></i>
    <div class="name">Baumpflege<br>Holstedt<span class="claim">Kronenpflege mit Seil</span></div>
  </div>
</section>
<section class="sheet navy" style="left:621px;top:384px;width:445px;height:277px">
  <div class="logo lime" style="left:60px;top:98px;font-size:26px">
    <i class="dot"></i>
    <div class="name">Baumpflege<br>Holstedt<span class="claim">Kronenpflege mit Seil</span></div>
  </div>
</section>

<!-- Business cards -->
<span class="label" style="left:174px;top:672px">1</span>
<section class="sheet card" style="left:198px;top:669px">
  <div class="logo green" style="left:14px;top:34px;font-size:9px">
    <i class="dot"></i>
    <div class="name">Baumpflege<br>Holstedt<span class="claim">Kronenpflege mit Seil</span></div>
  </div>
</section>
<span class="label" style="left:174px;top:787px">2</span>
<section class="sheet card navy" style="left:198px;top:783px">
  <div class="logo lime" style="left:14px;top:34px;font-size:9px">
    <i class="dot"></i>
    <div class="name">Baumpflege<br>Holstedt<span class="claim">Kronenpflege mit Seil</span></div>
  </div>
</section>

<span class="label" style="left:378px;top:672px">A</span>
<section class="sheet card" style="left:398px;top:669px">
  <div class="logo green" style="left:12px;top:32px;font-size:14px"><i class="dot"></i></div>
  <div class="details">
    <div class="person">JOHN DOE</div><div class="role">Geschäftsführer</div>
    BAUMPFLEGE HOLSTEDT<br>XXXXXXX Str. 00<br>00000 Germany
    <ul class="contact-list">
      <li><svg viewBox="0 0 10 10"><rect x="1" y="3" width="8" height="6" rx="1"/></svg>0000 00 00 00 00</li>
      <li><svg viewBox="0 0 10 10"><rect x="3" y="0" width="4" height="10" rx="1"/></svg>0000 00 00 00 00</li>
      <li><svg viewBox="0 0 10 10"><rect x="0" y="2" width="10" height="6"/></svg>info@baumpflege-holstedt.de</li>
    </ul>
  </div>
  <div class="band">www.baumpflege-holstedt.de</div>
</section>

<span class="label" style="left:378px;top:787px">B</span>
<section class="sheet card alt" style="left:398px;top:783px">
  <div class="logo green" style="left:12px;top:32px;font-size:14px"><i class="dot"></i></div>
  <div class="details">
    <div class="person">JOHN DOE</div><div class="role">Geschäftsführer</div>
    BAUMPFLEGE HOLSTEDT<br>XXXXXXX Str. 00<br>00000 Germany
    <ul class="contact-list">
      <li><svg viewBox="0 0 10 10"><rect x="1" y="3" width="8" height="6" rx="1"/></svg>0000 00 00 00 00</li>
      <li><svg viewBox="0 0 10 10"><rect x="3" y="0" width="4" height="10" rx="1"/></svg>0000 00 00 00 00</li>
      <li><svg viewBox="0 0 10 10"><rect x="0" y="2" width="10" height="6"/></svg>info@baumpflege-holstedt.de</li>
    </ul>
  </div>
  <div class="band navy">www.baumpflege-holstedt.de</div>
</section>

<!-- Envelopes -->
<span class="label" style="left:607px;top:694px">1</span>
<section class="sheet envelope" style="left:626px;top:689px">
  <div class="ghost-mark" style="left:200px;top:4px;width:170px;height:170px"></div>
  <div class="logo green" style="left:10px;top:10px;font-size:9px">
    <i class="dot"></i>
    <div class="name">Baumpflege<br>Holstedt<span class="claim">Kronenpflege mit Seil</span></div>
  </div>
  <div class="band">www.baumpflege-holstedt.de</div>
</section>

<span class="label" style="left:607px;top:914px">2</span>
<section class="sheet envelope" style="left:626px;top:911px">
  <div class="ghost-mark" style="left:200px;top:4px;width:170px;height:170px"></div>
  <div class="logo green" style="left:10px;top:10px;font-size:9px">
    <i class="dot"></i>
    <div class="name">Baumpflege<br>Holstedt<span class="claim">Kronenpflege mit Seil</span></div>
  </div>
  <div class="band navy">www.baumpflege-holstedt.de</div>
</section>

</body>
</html>
```